Larkmont Business Card Design Project

Double side card , just the logo on oxford white background on one side , and the rest of the information on the other side..
the company name is : Larkmont International General Trading LLC.
logo is already attached
the card to show in the info side: company name, employee name and position (job title) phone number, fax number, email address, P.O. box, Location (city and country)
deadline is already extended 4 all to have more time... thanks

```html
<!DOCTYPE html>
<html lang="en">
<head>
<meta charset="utf-8">
<title>Larkmont Int. — Business Card</title>
<link href="https://fonts.googleapis.com/css2?family=Questrial&display=swap" rel="stylesheet">
<style>
  :root {
    --page: #e8e6e3;
    --card: #ffffff;
    --blue: #1e8fc8;
    --ink: #3b3e43;
    --white: #ffffff;
  }
  * { margin: 0; padding: 0; box-sizing: border-box; }
  html, body { width: 1200px; height: 800px; overflow: hidden; }
  body {
    background: var(--page);
    font-family: "Questrial", "Century Gothic", sans-serif;
    position: relative;
  }
  .card {
    position: absolute;
    width: 554px;
    height: 322px;
    border-radius: 24px;
    background: var(--card);
    overflow: hidden;
    box-shadow: 0 2px 6px rgba(0,0,0,0.12);
  }
  .card--front { left: 240px; top: 92px; }
  .card--back { left: 239px; top: 429px; }

  .brand-name {
    position: absolute;
    color: var(--ink);
    font-family: "Questrial", "Century Gothic", sans-serif;
    font-weight: 400;
    letter-spacing: 1px;
    white-space: nowrap;
  }
  .card--front .brand-name {
    left: 0; right: 0; top: 180px;
    text-align: center;
    font-size: 40px;
  }
  .card--back .brand-name {
    left: 36px; top: 112px;
    font-size: 33px;
  }

  .card__band { position: absolute; inset: 0; }

  .holder {
    position: absolute;
    left: 37px; top: 256px;
    color: var(--white);
  }
  .holder__name { font-size: 18px; line-height: 22px; }
  .holder__title { font-size: 12px; line-height: 16px; }

  .contacts {
    position: absolute;
    right: 33px; top: 202px;
    list-style: none;
    color: var(--white);
    font-size: 12.5px;
  }
  .contacts li {
    display: flex;
    justify-content: flex-end;
    align-items: center;
    height: 19.5px;
    gap: 8px;
  }
  .contacts svg { width: 12px; height: 12px; flex: none; }
</style>
</head>
<body>

<section class="card card--front">
  <div class="brand-name">Larkmont Int.</div>
</section>

<section class="card card--back">
  <svg class="card__band" viewBox="0 0 554 322" width="554" height="322" aria-hidden="true">
    <path d="M0,190 Q330,210 554,40 L554,322 L0,322 Z" fill="var(--blue)"/>
  </svg>

  <div class="brand-name">Larkmont Int.</div>

  <div class="holder">
    <div class="holder__name">Daniel Hart</div>
    <div class="holder__title">General Manager</div>
  </div>

  <ul class="contacts">
    <li>555 210 4380
      <svg viewBox="0 0 12 12"><path d="M2.5 1 L4.5 1 L5.2 3.4 L4 4.4 C4.6 5.8 5.9 7.2 7.5 8 L8.5 6.8 L11 7.5 L11 9.5 C11 10.3 10.3 11 9.5 11 C5 10.8 1.2 7 1 2.5 C1 1.7 1.7 1 2.5 1 Z" fill="var(--white)"/></svg>
    </li>
    <li>555 210 4381
      <svg viewBox="0 0 12 12"><rect x="3" y="1" width="6" height="3" fill="var(--white)"/><rect x="1" y="4.5" width="10" height="4.5" rx="1" fill="var(--white)"/><rect x="3" y="8" width="6" height="3" fill="var(--white)" stroke="var(--blue)" stroke-width="0.8"/></svg>
    </li>
    <li>danielhart@larkmontint.com
      <svg viewBox="0 0 12 12"><rect x="1" y="2.5" width="10" height="7" fill="var(--white)"/><path d="M1 2.5 L6 6.5 L11 2.5" fill="none" stroke="var(--blue)" stroke-width="0.9"/></svg>
    </li>
    <li>www.larkmontint.com
      <svg viewBox="0 0 12 12"><circle cx="6" cy="6" r="5" fill="none" stroke="var(--white)" stroke-width="1.2"/><ellipse cx="6" cy="6" rx="2.2" ry="5" fill="none" stroke="var(--white)" stroke-width="1"/><path d="M1 6 H11" stroke="var(--white)" stroke-width="1"/></svg>
    </li>
    <li>8-10 Suite, Harwell Road, Brookfield 5678
      <svg viewBox="0 0 12 12"><path d="M6 11.5 C3.5 8 2 6.2 2 4.3 A4 4 0 0 1 10 4.3 C10 6.2 8.5 8 6 11.5 Z" fill="var(--white)"/><circle cx="6" cy="4.3" r="1.5" fill="var(--blue)"/></svg>
    </li>
  </ul>
</section>

</body>
</html>
```